Destination Wedding Photographer

I am a Wedding photographer based in San Juan, Puerto Rico. The banner will be shown in the United States to brides that plan to have their wedding in Puerto Rico.

I want to highlight the following words/phrases
Puerto Rico
Destination Wedding
Photographer
(in that order)

feel free to get creative adding your own inspired text.

My web site: www.benitolavarro.com

Target Market(s)

Brides in the united states looking for a photographer for their wedding in Puerto Rico

Industry/Entity Type

Wedding

Requirements
Must have
• + Your ad must be a .gif, .png or .jpg smaller than 40kb in filesize
+ include the following sizes: 300x250, 728x90, 160x600, 468x60, or 120x600
+ Your ad must include the advertiser's brand
+ Your ad must have a border
Should not have
• + Your ad cannot imitate computer effects like scrolling or mousing over
+ No animations longer than 30 seconds
+ No strobe or flashing effects allowed
+ Your ad and campaign must not feature or promote alcohol, anabolic steroids, drugs, financial products, gambling, adult content, or weight loss products

```html
<!DOCTYPE html>
<html lang="en">
<head>
<meta charset="UTF-8">
<title>Destination Wedding Puerto Rico – Benito Lavarro Photography</title>
<link rel="stylesheet" href="https://fonts.googleapis.com/css2?family=Questrial&family=Great+Vibes&family=Cinzel&display=swap">
<style>
  :root {
    --page: #ffffff;
    --frame: #1a1a1a;
    --ink: #ffffff;
    --panel-dark: #1f1a1d;
    --accent: #f2ea2e;
    --accent-shadow: #111111;
    --glow: rgba(150, 140, 200, 0.35);
    --sea-deep: #3f6f86;
    --sea-light: #8fb1bd;
    --gown: #eef0f2;
  }
  * { margin: 0; padding: 0; box-sizing: border-box; }
  html, body {
    width: 1200px; height: 900px; overflow: hidden;
    background: var(--page);
  }
  .banner {
    position: absolute; left: 113px; top: 48px;
    width: 938px; height: 785px;
    border: 2px solid var(--frame);
    background: var(--page);
  }
  .tile { position: absolute; }
  .photo-couple-sea {
    left: 9px; top: 14px; width: 410px; height: 760px;
    background:
      radial-gradient(ellipse at 60% 75%, var(--gown) 0%, rgba(238,240,242,0.85) 25%, rgba(238,240,242,0) 50%),
      radial-gradient(ellipse at 55% 25%, #c49a80 0%, rgba(196,154,128,0) 35%),
      linear-gradient(180deg, var(--sea-light) 0%, var(--sea-deep) 55%, #2e5669 100%);
  }
  .photo-centerpiece {
    left: 430px; top: 14px; width: 246px; height: 268px;
    background:
      radial-gradient(ellipse at 55% 30%, #f3ece4 0%, rgba(243,236,228,0) 45%),
      linear-gradient(180deg, #2a2522 0%, #6d6460 60%, #cfc8c2 100%);
  }
  .photo-first-dance {
    left: 688px; top: 14px; width: 240px; height: 258px;
    background:
      radial-gradient(ellipse at 30% 40%, #e7c7b0 0%, rgba(231,199,176,0) 40%),
      linear-gradient(90deg, #b9a08e 0%, #6f6d5e 55%, #1c1c1e 100%);
  }
  .panel-dark {
    left: 430px; top: 287px; width: 240px; height: 250px;
    background: radial-gradient(ellipse at 50% 50%, #2a2428 0%, var(--panel-dark) 100%);
    box-shadow: 0 0 18px var(--glow);
  }
  .photo-beach-ceremony {
    left: 677px; top: 282px; width: 251px; height: 255px;
    background:
      radial-gradient(ellipse at 45% 70%, #f5f5f5 0%, rgba(245,245,245,0) 30%),
      linear-gradient(180deg, #dfe6ee 0%, #b7c9d6 45%, #3fa3b4 62%, #e8d9c6 78%, #cdb59e 100%);
  }
  .panel-brand {
    left: 430px; top: 552px; width: 498px; height: 222px;
    background: var(--panel-dark);
    box-shadow: 0 0 18px var(--glow);
    color: var(--ink);
    text-align: center;
  }
  .headline-destination {
    position: absolute; left: 26px; top: 18px; height: 756px;
    writing-mode: vertical-rl; transform: rotate(180deg);
    font-family: "Questrial", "Century Gothic", sans-serif;
    font-size: 124px; line-height: 1; color: var(--ink);
    text-align: center; letter-spacing: 1px;
  }
  .headline-wedding {
    position: absolute; left: 210px; top: 118px;
    font-family: "Great Vibes", cursive;
    font-size: 210px; line-height: 1; color: var(--accent);
    text-shadow: -5px 4px 0 var(--accent-shadow);
    transform: rotate(-6deg);
  }
  .headline-place {
    position: absolute; left: 158px; top: 452px;
    font-family: "Questrial", "Century Gothic", sans-serif;
    font-size: 74px; line-height: 1; color: var(--ink);
    letter-spacing: -1px;
  }
  .brand-name {
    position: absolute; left: 0; right: 0; top: 62px;
    font-family: "Great Vibes", cursive;
    font-size: 72px; line-height: 1;
  }
  .brand-tag {
    position: absolute; left: 160px; width: 250px; top: 146px;
    font-family: "Cinzel", serif; font-size: 15px; letter-spacing: 4px;
    border-top: 1px solid var(--ink); border-bottom: 1px solid var(--ink);
    padding: 1px 0;
  }
  .brand-site {
    position: absolute; left: 0; right: 0; top: 176px;
    font-family: "Questrial", "Century Gothic", sans-serif;
    font-size: 30px; line-height: 1;
  }
</style>
</head>
<body>
  <main class="banner">
    <div class="tile photo-couple-sea" role="img" aria-label="Bride and groom laughing, waist deep in the sea, groom carrying the bride in her gown"></div>
    <div class="tile photo-centerpiece" role="img" aria-label="Reception table with white rose centerpiece in a glass vase"></div>
    <div class="tile photo-first-dance" role="img" aria-label="Bride and groom sharing their first dance"></div>
    <div class="tile panel-dark"></div>
    <div class="tile photo-beach-ceremony" role="img" aria-label="Beach wedding ceremony under a white canopy by the ocean"></div>
    <section class="tile panel-brand">
      <div class="brand-name">Benito Lavarro</div>
      <div class="brand-tag">PHOTOGRAPHY</div>
      <div class="brand-site">www.benitolavarro.com</div>
    </section>
    <h1 class="headline-destination">Destination</h1>
    <h2 class="headline-wedding">Wedding</h2>
    <p class="headline-place">Puerto Rico</p>
  </main>
</body>
</html>
```